Real Estate Marketing Postcards need a fresh look, Front & Back

I have a current postcard design (attached) that lacks design quality and too much use of color. I do like the basic color scheme, but I'm open to anything that cleans up the look and incorporates space for the existing text. I'm not opposed to a design with a white background, more white space. The design should be full bleed according to the attached specs. I would like this to be sent over in an Adobe format, something like InDesign.

The company logo will remain the same colors and appearance. The headshot will likely be updated in the coming weeks.

I am attaching a sample of a recent card plus a template from the printer showing the back of the card and location of the address and postage section that must remain blank. I am also including the logo and another logo designed for use with a white (or non blue) background.

(feel free to swap in stock photos of whatever house you want, but the front of the card should incorporate at least one photo of a house.)

Target Market(s)

Home owners.

Industry/Entity Type

Real Estate

Font styles to use
Sans Serif

Colors

Designer to choose colors to be used in the design.

Requirements
Must have
• Company logo, the headshot, the contact info on the back, a photo or photos of a house along with the text "Just Sold" or "Sold" featured on the front of the card.

```html
<!DOCTYPE html>
<html lang="en">
<head>
<meta charset="utf-8">
<title>Just Listed Postcard – Front &amp; Back</title>
<link rel="stylesheet" href="https://fonts.googleapis.com/css2?family=Montserrat:ital,wght@0,500;0,600;0,700;0,800;1,700&family=Roboto+Condensed:wght@700&display=swap">
<style>
  :root {
    --brand-blue: #1c5490;
    --ink: #1b1b1b;
    --panel-grey: #d9d9d9;
    --paper: #ffffff;
    --backdrop: #e9e9ea;
    --sky-top: #8f95c4;
    --sky-mid: #c8b7cf;
    --house-tone: #6d7487;
    --lawn: #6f8f4a;
    --portrait-bg: #a7a9ac;
    --divider: #a9a9a9;
  }
  * { box-sizing: border-box; margin: 0; padding: 0; }
  html, body { width: 1200px; height: 1000px; overflow: hidden; }
  body {
    background: var(--backdrop);
    font-family: "Montserrat", Arial, sans-serif;
    color: var(--ink);
    position: relative;
  }
  .postcard {
    position: absolute;
    left: 290px;
    width: 620px;
    height: 410px;
    background: var(--paper);
    overflow: hidden;
    box-shadow: 0 6px 14px rgba(0,0,0,0.18);
  }
  .postcard--front { top: 60px; }
  .postcard--back { top: 525px; }

  /* Front */
  .house-photo {
    position: absolute;
    left: 150px; top: 0;
    width: 470px; height: 250px;
    background:
      linear-gradient(90deg, #ffffff 0%, rgba(255,255,255,0) 28%),
      linear-gradient(180deg, var(--sky-top) 0%, var(--sky-mid) 35%, var(--house-tone) 60%, var(--lawn) 88%, #9aa0a6 100%);
  }
  .headline {
    position: absolute;
    left: 28px; top: 76px;
    width: 240px;
    text-align: center;
  }
  .headline__lead {
    font-weight: 600;
    font-size: 21px;
    line-height: 1.05;
    letter-spacing: 0.5px;
  }
  .headline__main {
    font-weight: 800;
    font-size: 54px;
    line-height: 0.9;
    color: var(--brand-blue);
    -webkit-text-stroke: 2px var(--paper);
    paint-order: stroke fill;
    text-shadow: 0 2px 4px rgba(0,0,0,0.35);
    margin-top: 6px;
  }
  .headline__by {
    font-weight: 600;
    font-size: 21px;
    margin-top: 4px;
    padding-left: 60px;
  }
  .front-band {
    position: absolute;
    left: 40px; right: 0; top: 280px;
    height: 80px;
    background: var(--brand-blue);
    color: var(--paper);
    padding: 14px 0 0 24px;
  }
  .front-band__name {
    font-weight: 700;
    font-size: 26px;
    letter-spacing: 0.3px;
    white-space: nowrap;
  }
  .front-band__tagline {
    font-weight: 500;
    font-size: 14px;
    margin: 2px 0 0 120px;
  }
  .agent-portrait {
    position: absolute;
    border: 4px solid var(--paper);
    background: radial-gradient(circle at 50% 40%, #c4b8ad 0%, var(--portrait-bg) 60%, #8d9094 100%);
    box-shadow: 0 1px 3px rgba(0,0,0,0.3);
  }
  .agent-portrait--front { left: 452px; top: 225px; width: 155px; height: 128px; }

  /* Back */
  .back-band {
    position: absolute;
    left: 0; right: 0; top: 22px;
    height: 58px;
    background: var(--brand-blue);
    color: var(--paper);
    display: flex;
    align-items: flex-end;
    padding: 0 0 4px 28px;
  }
  .back-band__title {
    font-weight: 800;
    font-size: 40px;
    line-height: 1;
    letter-spacing: 1px;
  }
  .back-band__subtitle {
    font-weight: 600;
    font-size: 15px;
    line-height: 1.05;
    margin: 0 0 12px 22px;
  }
  .back-intro {
    position: absolute;
    left: 28px; top: 86px; right: 20px;
    font-size: 11px;
    font-weight: 500;
    line-height: 1.3;
  }
  .back-intro p { white-space: nowrap; }
  .info-panel {
    position: absolute;
    left: 0; right: 0; top: 150px;
    height: 150px;
    background: var(--panel-grey);
  }
  .info-panel__cta {
    position: absolute;
    left: 28px; top: 6px;
    font-weight: 700;
    font-style: italic;
    font-size: 14px;
    color: var(--brand-blue);
  }
  .company-mark {
    position: absolute;
    left: 24px; top: 70px;
    width: 120px; height: 58px;
    background: var(--brand-blue);
    color: var(--paper);
    text-align: center;
    padding-top: 10px;
  }
  .company-mark__name { font-weight: 700; font-size: 11px; white-space: nowrap; }
  .company-mark__phone { font-weight: 700; font-size: 12px; margin-top: 6px; }
  .credential-badges {
    position: absolute;
    left: 26px; top: 133px;
    display: flex; gap: 6px;
  }
  .credential-badges span {
    width: 11px; height: 11px;
    background: var(--brand-blue);
  }
  .reasons {
    position: absolute;
    left: 152px; top: 38px;
    width: 136px;
    font-size: 9px;
    font-weight: 600;
    line-height: 1.2;
  }
  .reasons p + p { margin-top: 8px; }
  .panel-divider {
    position: absolute;
    left: 296px; top: 42px;
    width: 1px; height: 94px;
    background: var(--divider);
  }
  .agent-portrait--back { left: 306px; top: 44px; width: 118px; height: 92px; border-width: 0; }
  .agent-contact {
    position: absolute;
    left: 434px; top: 28px;
    font-size: 11px;
    font-weight: 600;
    line-height: 1.25;
  }
  .agent-contact__name {
    font-family: "Roboto Condensed", Arial, sans-serif;
    font-weight: 700;
    font-size: 18px;
    color: var(--brand-blue);
    margin-bottom: 2px;
  }
</style>
</head>
<body>

  <section class="postcard postcard--front" aria-label="Postcard front">
    <div class="house-photo" role="img" aria-label="Photo of a two-storey suburban house at dusk with lit windows and a front lawn"></div>
    <div class="headline">
      <p class="headline__lead">ANOTHER<br>HOME</p>
      <p class="headline__main">JUST<br>LISTED</p>
      <p class="headline__by">BY</p>
    </div>
    <div class="front-band">
      <p class="front-band__name">THE ASHGROVE REALTOR</p>
      <p class="front-band__tagline">You&nbsp; KNOW it won’t last long !</p>
    </div>
    <div class="agent-portrait agent-portrait--front" role="img" aria-label="Agent headshot"></div>
  </section>

  <section class="postcard postcard--back" aria-label="Postcard back">
    <div class="back-band">
      <h2 class="back-band__title">SELLING</h2>
      <p class="back-band__subtitle">Choosing the right agent is<br>critical to your success</p>
    </div>
    <div class="back-intro">
      <p>Your home is your biggest asset.</p>
      <p>You owe it to yourself to have every advantage by choosing the local agent with</p>
      <p>the expertise to position your Ashgrove home and get it sold fast and for top dollar.</p>
      <p>There is no other agent who knows the Ashgrove market better.</p>
    </div>
    <div class="info-panel">
      <p class="info-panel__cta">Contact me today to get your home sold.</p>
      <div class="company-mark">
        <p class="company-mark__name">Maple Run Realty</p>
        <p class="company-mark__phone">(555) 310-4400</p>
      </div>
      <div class="credential-badges" aria-hidden="true"><span></span><span></span></div>
      <div class="reasons">
        <p>There are 3 key reasons a home doesn’t sell, and #1 is choosing the wrong agent to market your property.</p>
        <p>Contact me today to discuss your home’s value and what steps I will take to assure your success</p>
      </div>
      <div class="panel-divider"></div>
      <div class="agent-portrait agent-portrait--back" role="img" aria-label="Agent headshot"></div>
      <div class="agent-contact">
        <p class="agent-contact__name">Dario Venturelli</p>
        <p>“The Ashgrove Realtor”</p>
        <p>Principal Broker, REALTOR</p>
        <p>Maple Run Realty</p>
        <p>O: (555) 310 4400</p>
        <p>C: (555) 604 2187</p>
        <p>www.ashgrovehomes.com</p>
      </div>
    </div>
  </section>

</body>
</html>
```